Vermilion Reel Works Web Design

COMPANY: VERMILION REEL WORKS
LOCATION: SHANGHAI, CHINA
AREA: FILM/TV DRAMA/COMMERCIALS/GAME POST PRODUCTION, SOUND DESIGN, MUSIC, and GAME.
WEB STYLE: SIMPLE, PROFESSIONAL, TRUSTWORTHY

LANGUAGE: ENGLISH, CHINESE. (Same layout, different language)
UPDATE: AFTER PROJECT FINISHED, WE NEED UPDATE BY OURSELVES.

MAIN SUBJECT: 6
1 HOMEPAGE
2 ABOUT US
3 TEAM
4 SERVICES
5 FACILITY
6 CONTACT

add one page of JOB OPPORTUNITIES.

DETAILS
1 HOMEPAGE
SLOGAN: Vermilion Reel Works provides a well-designed working environment which amplifies your team’s ability to reach their creative goals.

Our services include:
 Feature Films
 Music & Scoring
 Commercials
 ADR & Foley
 Sound & Picture Editorial
 Sound Design
 Video Game

2 ABOUT US
Vermilion Reel Works is located in the premiere South-Bund area of Shanghai. Occupying a 5000 square meter Technical Building, Vermilion Reel Works was built by a filmmaker for filmmakers, and is one of the largest, most versatile full-service post-production facilities in China.

Vermilion Reel Works is positioning to be at the forefront of the latest technology. Our goal is to provide a comprehensive solution for the post-production needs of our clients. We offer two fully-equipped dubbing stages (one of which will be certified KESTRON VOXAR PREMIERE), a large variety of both picture and sound editing rooms, impressive Foley and ADR stages, a world-class scoring stage, and complete audio and video transfer services.

We can handle your entire project from editing all the way to the end of the final sound mix; all under one extremely comfortable roof. We fully realize that the true art is in listening to the needs of our clients and making their greatest vision a reality. To this end our creative team's expertise, with a network of sound supervisors, editors and mixers, will deliver the magic you need. Producers and directors will also find our richly appointed guest accommodations to be a comfortable and soothing place to wind up the day. Every aspect of your project will be taken care of by a skilled and dedicated team, in the way that is best suited to you.

3 TEAM
(attachment 01)

4 SERVICES
Sound Mix
ADR
FOLEY
MUSIC
Sound Design
Sound Edit
Picture Edit
for all the Films, TV Drama, Commercials, Video Games, Online Media
(attachment 02, use photo)

5 FACILITY
(attachment 03)

6 CONTACT
(attachment04)
with map

Project Deadline Extended
Reason: Designers work are great, my bosses will spend 1-2 days select one of these web design, and spend 1-2 days to make some change, maybe use new photos.

```html
<!DOCTYPE html>
<html lang="en">
<head>
<meta charset="utf-8">
<title>Vermilion Reel Works</title>
<link href="https://fonts.googleapis.com/css2?family=Open+Sans:wght@400;600;700;800&display=swap" rel="stylesheet">
<style>
:root{
  --ink:#2b2b2b;
  --muted:#777;
  --white:#fff;
  --band:#1e2024;
  --band-edge:#34373c;
  --accent:#2f6fb6;
  --heading:#2a4f86;
  --footer:#2a2b2e;
  --rule:#d9d9d9;
}
*{box-sizing:border-box;margin:0;padding:0}
html,body{width:766px;height:1200px;overflow:hidden}
body{font-family:"Open Sans",Arial,sans-serif;color:var(--ink);background:var(--white);position:relative}

.site-header{height:38px;display:flex;align-items:center;padding:0 20px 0 64px;background:var(--white)}
.brand{display:flex;align-items:center;gap:5px;font-weight:700;font-size:9px;color:var(--accent);letter-spacing:.3px;margin-right:60px}
.brand-mark{width:12px;height:12px;background:var(--accent)}
.main-nav{display:flex;gap:22px;font-size:6.5px;font-weight:600;color:#555;letter-spacing:.3px}
.lang-select{margin-left:24px;width:48px;height:14px;border:1px solid #ccc;font-size:6px;display:flex;align-items:center;justify-content:space-between;padding:0 4px;color:#555}
.search-btn{margin-left:10px;width:14px;height:14px}

.hero{position:relative;height:460px}
.hero-photo{position:absolute;inset:0;background:linear-gradient(120deg,#3a3f46 0%,#1d2127 45%,#4a4640 70%,#141619 100%)}
.hero-copy{position:absolute;left:0;right:0;top:255px;text-align:center;color:var(--white)}
.hero-title{font-size:24px;font-weight:800;letter-spacing:.5px}
.hero-slogan{margin:12px auto 0;width:430px;font-size:11.5px;font-weight:600;line-height:16px}

.welcome{height:115px;text-align:center;padding-top:36px}
.welcome h2{font-size:12px;font-weight:600;letter-spacing:.4px;color:#333}
.welcome p{width:548px;margin:10px auto 0;font-size:6px;line-height:10px;color:var(--muted)}

.services{height:166px;background:var(--band);text-align:center;padding-top:32px}
.services h2{font-size:12px;font-weight:700;color:var(--white);letter-spacing:.5px}
.services .rule{width:30px;height:1px;background:#777;margin:6px auto 0}
.service-list{display:flex;gap:14px;justify-content:center;margin-top:22px}
.service-card{width:98px;height:64px;border:1px solid var(--band-edge);color:var(--white);display:flex;flex-direction:column;align-items:center;justify-content:center;gap:4px}
.service-card.is-active{background:var(--accent);border-color:var(--accent)}
.service-card strong{font-size:7px;font-weight:700;letter-spacing:.3px}
.service-card span{font-size:4.5px;color:#cfd6e0}

.gallery{width:548px;margin:0 auto}
.gallery-head{display:flex;justify-content:space-between;align-items:center;border-bottom:1px solid var(--rule);padding-bottom:5px}
.gallery-head h2{font-size:12px;font-weight:600;color:var(--heading)}
.arrows{display:flex;gap:6px}
.gallery-intro{font-size:5.5px;color:var(--muted);margin-top:8px;line-height:9px}
.gallery-row{display:flex;gap:10px;margin-top:12px}
.tile{width:129.5px}
.tile-photo{height:74px}
.tile p{font-size:5.5px;font-weight:700;margin-top:5px;color:#333}
.films{padding-top:30px}
.music{padding-top:28px}

.site-footer{position:absolute;left:0;right:0;bottom:0;height:32px;background:var(--footer);display:flex;align-items:center;padding:0 110px;color:#aaa;font-size:5px}
.site-footer .legal{flex:1}
.social{display:flex;gap:5px}
.social i{width:11px;height:11px;border:1px solid #888;border-radius:50%;display:block}
.to-top{margin-left:14px;width:16px;height:12px;background:#444}
</style>
</head>
<body>
<header class="site-header">
  <div class="brand"><span class="brand-mark"></span>Vermilion Reel Works</div>
  <nav class="main-nav">
    <span>HOME</span><span>ABOUT US</span><span>TEAM</span><span>SERVICES</span><span>FACILITY</span><span>JOB OPPORTUNITIES</span><span>CONTACT US</span>
  </nav>
  <div class="lang-select">ENGLISH <span>▾</span></div>
  <svg class="search-btn" viewBox="0 0 14 14"><circle cx="6" cy="6" r="3.5" fill="none" stroke="#666" stroke-width="1.2"/><line x1="8.6" y1="8.6" x2="12" y2="12" stroke="#666" stroke-width="1.2"/></svg>
</header>

<section class="hero">
  <div class="hero-photo" role="img" aria-label="Sound engineer working at a mixing console in a dim studio"></div>
  <div class="hero-copy">
    <h1 class="hero-title">VERMILION REEL WORKS</h1>
    <p class="hero-slogan">VERMILION REEL WORKS PROVIDES A WELL-DESIGNED WORKING ENVIRONMENT WHICH AMPLIFIES YOUR TEAM'S ABILITY TO REACH THEIR CREATIVE GOALS.</p>
  </div>
</section>

<section class="welcome">
  <h2>WELCOME TO VERMILION REEL WORKS</h2>
  <p>VERMILION REEL WORKS IS LOCATED IN THE PREMIERE SOUTH-BUND AREA OF SHANGHAI. OCCUPYING A 5000 SQUARE METER TECHNICAL BUILDING, VERMILION REEL WORKS WAS BUILT BY A FILMMAKER FOR FILMMAKERS, AND IS ONE OF THE LARGEST, MOST VERSATILE FULL-SERVICE POST-PRODUCTION FACILITIES IN CHINA.</p>
</section>

<section class="services">
  <h2>WHAT WE DO</h2>
  <div class="rule"></div>
  <div class="service-list">
    <div class="service-card is-active"><strong>COMMERCIALS</strong><span>CLICK HERE FOR MORE DETAILS</span></div>
    <div class="service-card"><strong>ADR &amp; FOLEY</strong><span>CLICK HERE FOR MORE DETAILS</span></div>
    <div class="service-card"><strong>SOUND &amp; PICTURE EDITORIAL</strong><span>CLICK HERE FOR MORE DETAILS</span></div>
    <div class="service-card"><strong>SOUND DESIGN</strong><span>CLICK HERE FOR MORE DETAILS</span></div>
    <div class="service-card"><strong>VIDEO GAME</strong><span>CLICK HERE FOR MORE DETAILS</span></div>
  </div>
</section>

<section class="gallery films">
  <div class="gallery-head">
    <h2>FEATURED FILMS</h2>
    <div class="arrows"><svg width="8" height="8" viewBox="0 0 8 8"><path d="M5 1 2 4l3 3" fill="none" stroke="#888"/></svg><svg width="8" height="8" viewBox="0 0 8 8"><path d="M3 1l3 3-3 3" fill="none" stroke="#888"/></svg></div>
  </div>
  <p class="gallery-intro">FEATURE FILM POST PRODUCTION, SOUND MIX AND PICTURE EDIT IN ONE BUILDING IN SHANGHAI.</p>
  <div class="gallery-row">
    <div class="tile"><div class="tile-photo" role="img" aria-label="Film still in warm tones" style="background:linear-gradient(135deg,#5a4a3e,#c9a98a)"></div><p>LOREM IPSUM IS SIMPLY</p></div>
    <div class="tile"><div class="tile-photo" role="img" aria-label="Silhouette against a pale sky" style="background:linear-gradient(180deg,#d8d8d8,#4a4a4a)"></div><p>LOREM IPSUM IS SIMPLY</p></div>
    <div class="tile"><div class="tile-photo" role="img" aria-label="Colourful film scene" style="background:linear-gradient(135deg,#3a6a9a,#d9a24a)"></div><p>LOREM IPSUM IS SIMPLY</p></div>
    <div class="tile"><div class="tile-photo" role="img" aria-label="Dark dramatic film still" style="background:linear-gradient(135deg,#1e1e1e,#6a5a4a)"></div><p>LOREM IPSUM IS SIMPLY</p></div>
  </div>
</section>

<section class="gallery music">
  <div class="gallery-head">
    <h2>MUSIC &amp; SCORING</h2>
    <div class="arrows"><svg width="8" height="8" viewBox="0 0 8 8"><path d="M5 1 2 4l3 3" fill="none" stroke="#888"/></svg><svg width="8" height="8" viewBox="0 0 8 8"><path d="M3 1l3 3-3 3" fill="none" stroke="#888"/></svg></div>
  </div>
  <p class="gallery-intro">MUSIC RECORDING AND SCORING ON A WORLD-CLASS STAGE FOR FILM, TV AND GAMES.</p>
  <div class="gallery-row">
    <div class="tile"><div class="tile-photo" role="img" aria-label="Musical instrument close-up" style="background:linear-gradient(135deg,#2a2a2a,#9a9a9a)"></div><p>LOREM IPSUM IS SIMPLY</p></div>
    <div class="tile"><div class="tile-photo" role="img" aria-label="Musician wearing headphones" style="background:linear-gradient(135deg,#b5b5b5,#3a3a3a)"></div><p>LOREM IPSUM IS SIMPLY</p></div>
    <div class="tile"><div class="tile-photo" role="img" aria-label="Blue lit stage performance" style="background:linear-gradient(135deg,#1a3a6a,#6aa0d0)"></div><p>LOREM IPSUM IS SIMPLY</p></div>
    <div class="tile"><div class="tile-photo" role="img" aria-label="Vinyl turntable in amber light" style="background:linear-gradient(135deg,#2a1a0a,#c8802a)"></div><p>LOREM IPSUM IS SIMPLY</p></div>
  </div>
</section>

<footer class="site-footer">
  <div class="legal">COPYRIGHT 2014 VERMILION REEL WORKS. ALL RIGHTS RESERVED &nbsp;|&nbsp; PRIVACY POLICY &nbsp;|&nbsp; TERMS &amp; CONDITIONS</div>
  <div class="social"><i></i><i></i><i></i></div>
  <svg class="to-top" viewBox="0 0 16 12"><rect width="16" height="12" fill="#444"/><path d="M5 7l3-3 3 3" fill="none" stroke="#bbb"/></svg>
</footer>
</body>
</html>
```